Education related business need name card design

We need name card design for long term study agent.
Company name is Harbor Lantern.
We support clients to connect to the world.
Clients are Japanese family who has primary and secondary school students.

Company Logo is reflection of the globe and HL (Harbor Lantern).
Since business is related to education, we would like to show reliability and love to see the world map (atlas) in the name card.

Target Market(s)

late 30's to 50's parents of primary and secondary students who are enthusiastic for education. Secondary school management

Industry/Entity Type

Education

Contact Information for Business Card

Company name, Address, Official position, Name, Phone number, Mobile number, email address,

Font styles to use
Serif
Other font styles liked:
• Century Gothic(logo)

Requirements
Must have
• Since businee is related to education, we would like to show reliability and love to see the world map (atlas) in the name card.

```html
<!DOCTYPE html>
<html lang="en">
<head>
<meta charset="utf-8">
<title>Harbor Lantern – Name Card</title>
<link href="https://fonts.googleapis.com/css2?family=Noto+Serif:ital,wght@0,400;0,700;1,400&display=swap" rel="stylesheet">
<style>
  :root {
    --navy: #033580;
    --navy-deep: #0a3a8a;
    --sky: #1479cf;
    --sky-light: #4fa3e8;
    --ink: #2b2b2b;
    --paper: #ffffff;
    --backdrop: #e6e7e9;
    --edge: #d4d6da;
  }
  * { box-sizing: border-box; margin: 0; padding: 0; }
  html, body { width: 1200px; height: 1200px; overflow: hidden; }
  body {
    background: var(--backdrop);
    font-family: "Noto Serif", Georgia, serif;
    display: flex;
    flex-direction: column;
    align-items: center;
    justify-content: center;
    gap: 44px;
  }
  .card {
    width: 900px;
    height: 514px;
    position: relative;
    overflow: hidden;
    border: 1px solid var(--edge);
  }

  /* Front */
  .card--front {
    background: var(--navy);
    display: flex;
    align-items: center;
    padding-left: 122px;
    gap: 26px;
  }
  .brand-dot {
    width: 160px; height: 160px;
    border-radius: 50%;
    background: var(--sky);
    flex: none;
  }
  .brand-name {
    color: var(--paper);
    font-size: 48px;
    line-height: 1.08;
    font-weight: 400;
  }

  /* Back */
  .card--back {
    background: var(--paper);
    display: flex;
  }
  .back-panel {
    width: 306px;
    background: var(--navy);
    position: relative;
    flex: none;
  }
  .world-globe {
    position: absolute;
    left: 44px; top: 92px;
    width: 220px; height: 220px;
    border-radius: 50%;
    background: radial-gradient(circle at 38% 35%, var(--sky-light), var(--sky) 70%);
  }
  .panel-brand {
    position: absolute;
    left: 46px; bottom: 48px;
    display: flex; align-items: center; gap: 10px;
    color: var(--paper);
    font-size: 15px;
    line-height: 1.15;
  }
  .panel-brand .mini-dot {
    width: 42px; height: 42px; border-radius: 50%;
    background: var(--paper);
    flex: none;
  }
  .details {
    padding: 112px 0 0 64px;
  }
  .person-name {
    font-weight: 700;
    font-size: 52px;
    line-height: 1.05;
    color: var(--navy-deep);
  }
  .name-rule {
    width: 78px; height: 7px;
    background: var(--sky);
    margin-top: 6px;
  }
  .role {
    font-size: 24px;
    font-style: italic;
    color: var(--ink);
    margin-top: 6px;
  }
  .company {
    font-size: 19px;
    color: var(--sky);
    margin-top: 2px;
  }
  .contacts {
    list-style: none;
    margin-top: 24px;
  }
  .contacts li {
    display: flex; align-items: center; gap: 10px;
    font-size: 16px;
    color: var(--ink);
    height: 41px;
    white-space: nowrap;
  }
  .contacts svg { width: 18px; height: 18px; fill: var(--navy-deep); flex: none; }
</style>
</head>
<body>

<section class="card card--front">
  <span class="brand-dot"></span>
  <p class="brand-name">Harbor Lantern<br>Pte.Ltd.</p>
</section>

<section class="card card--back">
  <div class="back-panel">
    <div class="world-globe" role="img" aria-label="World map atlas shown as a blue globe"></div>
    <div class="panel-brand">
      <span class="mini-dot"></span>
      <span>Harbor Lantern<br>Pte.Ltd.</span>
    </div>
  </div>
  <div class="details">
    <h1 class="person-name">Kenji Aldous</h1>
    <div class="name-rule"></div>
    <p class="role">Founder, COO</p>
    <p class="company">Harbor Lantern Pte. Ltd.</p>
    <ul class="contacts">
      <li>
        <svg viewBox="0 0 20 20"><path d="M10 2 1 9h3v8h5v-5h2v5h5V9h3z"/></svg>
        lorem Ipsum Street Dolor Amet City of Singapore
      </li>
      <li>
        <svg viewBox="0 0 20 20"><path d="M2 6c0-2 3-3 8-3s8 1 8 3v2h-4V6H6v2H2zM4 9h12l2 8H2z"/></svg>
        0000 12345 / 0000 12346 / 0000 12347
      </li>
      <li>
        <svg viewBox="0 0 20 20"><path d="M6 1h8a1 1 0 0 1 1 1v16a1 1 0 0 1-1 1H6a1 1 0 0 1-1-1V2a1 1 0 0 1 1-1zm1 2v12h6V3zm3 13a1 1 0 1 0 0 2 1 1 0 0 0 0-2z"/></svg>
        0000 9876543
      </li>
      <li>
        <svg viewBox="0 0 20 20"><path d="M1 4h18v12H1zm2 2v1l7 5 7-5V6l-7 5z"/></svg>
        kenji@harborlantern.com
      </li>
    </ul>
  </div>
</section>

</body>
</html>
```